Business Card Design

We need a new buisness card designed for a new company in Darwin
We dig trenchs and lay pipes for the communication industry,Electrical industry, Teleco industry,
We also do some concrete works as well,
And small excavation work
Communication
Belvanti Contracting PTY LTD
Pit and Pipe installations
Trenching,Excavations, Concreting ,
civil works, unistrut soloutions ,over thirty years experiance
NO TRENCH TOO DEEP, NO PIPE TOO LONG
Contact Glen 0491536208 ps
(would like name to stand out somehow in another text or graphic sort of a way am also looking for some sort of slogan) will most likely be a red card with black writing

```html
<!DOCTYPE html>
<html lang="en">
<head>
<meta charset="utf-8">
<title>Belvanti Contracting – Business Card</title>
<link rel="stylesheet" href="https://fonts.googleapis.com/css2?family=Open+Sans:wght@400;600;700;800&display=swap">
<style>
  :root {
    --page-bg: #e6e6e6;
    --card-black: #1b1b1b;
    --card-charcoal: #2a2a2a;
    --red-bright: #ec1c24;
    --red-mid: #d8161d;
    --red-deep: #a80f14;
    --ink: #1a1a1a;
  }
  * { box-sizing: border-box; margin: 0; padding: 0; }
  html, body {
    width: 1200px; height: 1000px; overflow: hidden;
    background: var(--page-bg);
    font-family: "Open Sans", Arial, sans-serif;
  }
  .business-card {
    position: absolute; left: 100px; top: 200px;
    width: 1000px; height: 600px;
    background: var(--card-black);
    box-shadow: 0 10px 30px rgba(0,0,0,.25);
    overflow: hidden;
  }
  .top-band {
    position: absolute; left: 0; top: 0; width: 100%; height: 34px;
    background: linear-gradient(to bottom, var(--card-charcoal) 0 14px, var(--card-black) 14px);
  }
  .identity-panel {
    position: absolute; left: 0; top: 34px; width: 100%; height: 336px;
    background: linear-gradient(to bottom, var(--red-bright), var(--red-mid) 60%, var(--red-deep));
  }
  .divider { position: absolute; left: 0; top: 370px; width: 100%; height: 4px; background: var(--card-black); }
  .contact-panel {
    position: absolute; left: 0; top: 374px; width: 100%; height: 136px;
    background: linear-gradient(to bottom, var(--red-bright), var(--red-mid) 55%, var(--red-deep));
  }
  .slogan-band { position: absolute; left: 0; top: 510px; width: 100%; height: 90px; background: var(--card-black); }
  .notch { position: absolute; left: 186px; top: 496px; }

  .company-name {
    position: absolute; left: 40px; top: 82px; width: 440px;
    color: var(--ink); text-align: center; line-height: 1;
  }
  .company-name .name-main { display: block; font-size: 74px; font-weight: 700; letter-spacing: 1px; }
  .company-name .name-sub { display: block; font-size: 50px; font-weight: 700; margin-top: 10px; }
  .company-name .name-legal { display: block; font-size: 48px; font-weight: 400; margin-top: 16px; letter-spacing: 1px; }

  .services {
    position: absolute; left: 524px; top: 92px;
    list-style: none; color: var(--ink);
  }
  .services li { font-size: 33px; line-height: 46px; font-weight: 400; }
  .services li::before { content: "• "; }
  .services .highlight { font-size: 24px; font-weight: 700; line-height: 44px; }

  .contact {
    position: absolute; left: 76px; top: 386px;
    display: flex; align-items: center; gap: 14px;
    color: var(--ink); white-space: nowrap;
  }
  .contact-name { font-size: 88px; font-weight: 700; letter-spacing: -1px; }
  .contact-phone { font-size: 80px; font-weight: 600; letter-spacing: 3px; }

  .slogan {
    position: absolute; left: 0; top: 536px; width: 100%;
    text-align: center; color: var(--red-bright);
    font-size: 35px; font-weight: 700; letter-spacing: 1.5px;
  }
</style>
</head>
<body>
  <div class="business-card">
    <div class="top-band"></div>
    <div class="identity-panel"></div>
    <div class="divider"></div>
    <div class="contact-panel"></div>
    <div class="slogan-band"></div>
    <svg class="notch" width="32" height="16" viewBox="0 0 32 16"><polygon points="0,16 16,0 32,16" fill="var(--card-black)"/></svg>

    <h1 class="company-name">
      <span class="name-main">BELVANTI</span>
      <span class="name-sub">CONTRACTING</span>
      <span class="name-legal">PTY LTD</span>
    </h1>

    <ul class="services">
      <li>Pit and Pipe installations</li>
      <li>Trenching</li>
      <li>Excavations</li>
      <li>concreting civil works</li>
      <li class="highlight">OVER 30 YEARS EXPERIANCE</li>
    </ul>

    <div class="contact">
      <span class="contact-name">Glen</span>
      <svg width="34" height="22" viewBox="0 0 34 22" aria-hidden="true">
        <line x1="0" y1="11" x2="24" y2="11" stroke="var(--ink)" stroke-width="3.5"/>
        <polygon points="20,3 34,11 20,19" fill="var(--ink)"/>
      </svg>
      <span class="contact-phone">0491 536 208</span>
    </div>

    <p class="slogan">NO TRENCH TOO DEEP, NO PIPE TOO LONG</p>
  </div>
</body>
</html>
```